We need a banner ad design for a company based in Brazil called "Zunaro" (http://www.zunaro-exemplo.com.br), which offers escort services for men. Our main strength and focus is helping people easily search for escorts using mobile devices, by being an mobile optimized repository of escorts which are crawled from many non-mobile optimized sites.

Target Market(s)

Men at all ages (above 18) looking for escorts

Industry/Entity Type

Escort

Requirements
Must have
• Size must be 468x60
The logo must be on white background
Nice to have
• The banner could have an eye-catching animation

The banner could have a small and quick animation showing the usage of the mobile application (like navigating through the application).
Should not have
• If animated then the text should not be split between frames.

```html
<!DOCTYPE html>
<html lang="pt-BR">
<head>
<meta charset="utf-8">
<title>Zunaro — banners 468x60</title>
<link rel="stylesheet" href="https://fonts.googleapis.com/css2?family=Fira+Sans:wght@500;600&display=swap">
<style>
  :root {
    --bg-center: #ffffff;
    --bg-edge: #b9b9b9;
    --brand-red: #980a15;
    --brand-red-dark: #7a0610;
    --frame: #1a1a1a;
    --text-light: #ffffff;
    --logo-white: #ffffff;
  }
  * { margin: 0; padding: 0; box-sizing: border-box; }
  html, body {
    width: 1200px;
    height: 1000px;
    overflow: hidden;
  }
  body {
    position: relative;
    background: radial-gradient(ellipse 62% 68% at 50% 50%, var(--bg-center) 55%, #ececec 78%, var(--bg-edge) 100%);
    font-family: "Fira Sans", Arial, sans-serif;
  }
  .banner {
    position: absolute;
    left: 355px;
    width: 468px;
    height: 60px;
    background: var(--brand-red);
    border: 1px solid var(--frame);
    overflow: hidden;
  }
  .banner--names { top: 348px; }
  .banner--promo { top: 558px; }

  .name-list {
    list-style: none;
    position: absolute;
    top: 1px;
    color: var(--text-light);
    font-weight: 600;
    font-size: 14.5px;
    line-height: 19.5px;
    letter-spacing: -0.1px;
  }
  .name-list:nth-child(1) { left: 13px; }
  .name-list:nth-child(2) { left: 107px; }
  .name-list:nth-child(3) { left: 200px; }
  .name-list:nth-child(4) { left: 294px; }
  .name-list:nth-child(5) { left: 387px; }

  .logo-panel {
    position: absolute;
    left: 7px;
    top: 0;
    width: 110px;
    height: 58px;
    background: var(--logo-white);
    display: flex;
    align-items: center;
    justify-content: center;
    gap: 6px;
  }
  .logo-mark {
    width: 12px;
    height: 12px;
    border-radius: 50%;
    background: var(--brand-red);
  }
  .logo-name {
    color: var(--brand-red);
    font-weight: 600;
    font-size: 20px;
  }
  .figure-area {
    position: absolute;
    left: 118px;
    top: 0;
    width: 42px;
    height: 58px;
    background: linear-gradient(180deg, #f4f4f4, #dddddd);
    clip-path: polygon(40% 0, 70% 0, 80% 30%, 75% 100%, 25% 100%, 20% 40%);
  }
  .promo-text {
    position: absolute;
    left: 160px;
    right: 0;
    top: 9px;
    text-align: center;
    color: var(--text-light);
    font-weight: 500;
    font-size: 17.5px;
    line-height: 21px;
  }
</style>
</head>
<body>
  <section class="banner banner--names" aria-label="Perfis em destaque">
    <ul class="name-list"><li>Isabella</li><li>Sophia</li><li>Emma</li></ul>
    <ul class="name-list"><li>Layla</li><li>Allison</li><li>Evelyn</li></ul>
    <ul class="name-list"><li>Olivia</li><li>Ava</li><li>Emily</li></ul>
    <ul class="name-list"><li>Brooklyn</li><li>Kaylee</li><li>Taylor</li></ul>
    <ul class="name-list"><li>Abigail</li><li>Madison</li><li>Chloe</li></ul>
  </section>

  <section class="banner banner--promo" aria-label="Zunaro">
    <div class="logo-panel">
      <span class="logo-mark"></span>
      <span class="logo-name">Zunaro</span>
    </div>
    <div class="figure-area" role="img" aria-label="Silhueta branca de uma mulher em pé"></div>
    <p class="promo-text">O maior catálogo de acompanhantes<br>na palma da sua mão</p>
  </section>
</body>
</html>
```